TressFlinger Labels for Hair Care Product

I am looking for a designer to help design a few labels for my hair care products for my natural hair care line. The labels should look very classy and high end. but, I am open to other options. I have 7 different hair products and they are Pebblo fern Rinse, Velvety Purifying Detangler, Zip Zap Coil Jellyfix, Whirl-o-Berry Hair Silk, Pecanza Deep Conditioner, Marigold Hydrate Whipfluff and Sunrise Quench Elixir. I need a label designed for each one.

Placed on a Bullet/Cosmo Bottle
• Sunrise Quench Elixir is a 6 oz., label size: 5.25 x 4.375 inches (w x h)

• The Pebblo Fern Rinse 8 oz, label size: 5.6875 x 5 inches (w x h)

• Zip Zap Coil Jellyfix 8 oz, label size: 5.6875 x 5 inches (w x h)

• Whirl-o-Berry Hair Silk 8 oz, label size: 5.6875 x 5 inches (w x h)

• Velvety Purifying Detangler 12 oz, label size: 6.75 x 5.125 inches (w x h)

Placed on a Jar
• The Pecanza Deep Conditioner is a 12 oz., label size:11.3125 x 1.6875 inches (w x h)
• Marigold Hydrate Whip is an 8 oz, label size:11.3125 x 0.875 inches (w x h)

Bleeds should be 1/8 inch. This labels are just for the front of the bottles.

I inserted two pictures of ideas for the labels. I absolutely love the font used on the first photo and the second photo is very similar to the classy labels I had in mind. I will let you know the Directions and the ingredients since it too much to put in the description. Thank you.

Target Market(s)

women with natural and relaxed hair

Industry/Entity Type

Hair

Font styles to use
Decorative
Script

Colors
a54499
ecdaeb
b768aa
e4daeb

Requirements
Must have
• I would love for half of the label to be clear with white on the bottom. Maybe a Gray lattice design on the white part. Must have a font similar to the font used in the logo.
Nice to have
• Gray trim around the labels

```html
<!DOCTYPE html>
<html lang="en">
<head>
<meta charset="utf-8">
<title>TressFlinger — Sunrise Quench Label</title>
<link rel="stylesheet" href="https://fonts.googleapis.com/css2?family=Cinzel:wght@400;500&family=Pinyon+Script&display=swap">
<style>
  :root {
    --label-stone: #dcd9d3;
    --label-white: #ffffff;
    --plum: #5b1a4b;
    --ink-soft: #b4b0ab;
    --ink-mid: #6f6b67;
    --ink-dark: #3a3836;
    --meadow-light: #ecebea;
    --meadow-deep: #cfcdcb;
    --rule-grey: #8d8a86;
  }
  html, body {
    margin: 0;
    padding: 0;
    width: 1001px;
    height: 1200px;
    overflow: hidden;
    background: var(--label-stone);
  }
  .label {
    position: relative;
    width: 1001px;
    height: 1200px;
    background: var(--label-stone);
    font-family: "Cinzel", serif;
    overflow: hidden;
  }
  .white-band {
    position: absolute;
    left: 0;
    top: 694px;
    width: 1001px;
    height: 400px;
    background: var(--label-white);
  }
  .meadow {
    position: absolute;
    left: 0;
    top: 790px;
    width: 1001px;
    height: 410px;
    background: linear-gradient(180deg, rgba(236,235,234,0) 0%, var(--meadow-light) 35%, var(--meadow-deep) 100%);
  }
  .ingredients {
    position: absolute;
    left: 70px;
    top: 118px;
    width: 320px;
    margin: 0;
    color: var(--ink-soft);
    font-size: 21px;
    line-height: 32px;
    letter-spacing: 0.2px;
  }
  .ingredients-heading {
    display: block;
  }
  .product-name {
    position: absolute;
    left: 430px;
    top: 150px;
    width: 560px;
    margin: 0;
    color: var(--plum);
    font-family: "Pinyon Script", cursive;
    font-weight: 400;
    font-size: 128px;
    line-height: 135px;
    text-align: center;
  }
  .product-name span { display: block; }
  .brand-seal {
    position: absolute;
    left: 620px;
    top: 582px;
    width: 232px;
    height: 232px;
  }
  .brand-name {
    position: absolute;
    left: 620px;
    top: 680px;
    width: 232px;
    margin: 0;
    text-align: center;
    color: var(--plum);
    font-family: "Cinzel", serif;
    font-weight: 500;
    font-size: 26px;
    line-height: 36px;
  }
  .volume {
    position: absolute;
    left: 137px;
    top: 822px;
    width: 200px;
    margin: 0;
    text-align: center;
    color: var(--ink-dark);
    font-size: 30px;
    line-height: 40px;
  }
  .volume-note {
    position: absolute;
    left: 40px;
    top: 896px;
    width: 300px;
    margin: 0;
    text-align: center;
    color: var(--ink-dark);
    font-size: 17px;
    line-height: 19px;
  }
  .divider {
    position: absolute;
    left: 359px;
    top: 800px;
    width: 2px;
    height: 132px;
    background: var(--rule-grey);
  }
  .tagline {
    position: absolute;
    left: 405px;
    top: 910px;
    width: 540px;
    margin: 0;
    text-align: center;
    color: var(--ink-mid);
    font-size: 30px;
    line-height: 40px;
  }
  .tagline-sub {
    position: absolute;
    left: 400px;
    top: 950px;
    width: 550px;
    margin: 0;
    text-align: center;
    color: var(--ink-soft);
    font-size: 19px;
    line-height: 26px;
    letter-spacing: 0.3px;
  }
</style>
</head>
<body>
<main class="label">
  <div class="white-band"></div>
  <div class="meadow" role="img" aria-label="Soft grey silhouette of wildflowers and tall grasses along the bottom of the label"></div>

  <p class="ingredients">
    <span class="ingredients-heading">Ingridients:</span>
    Sed ut perspiciatis unde omnis iste natus error sit voluptatem accusantium doloremque laudantium, totam rem aperiam, eaque ipsa quae ab illo inventore veritatis et quasi architecto beatae vitae dicta sunt explicabo. Nemo enim ipsam voluptatem quia voluptas sit aspernatur aut odit aut fugit, sed
  </p>

  <h1 class="product-name"><span>Sunrise</span><span>Quench</span></h1>

  <svg class="brand-seal" viewBox="0 0 232 232" aria-hidden="true">
    <circle cx="116" cy="116" r="114" fill="#ffffff" stroke="#c9c6c2" stroke-width="2"/>
  </svg>
  <p class="brand-name">TressFlinger</p>

  <p class="volume">6 oz</p>
  <p class="volume-note">et dolore magna aliqua,<br>ut enim ad minim veniam</p>
  <div class="divider"></div>

  <p class="tagline">Lorem ipsum dolor sit amet</p>
  <p class="tagline-sub">sed do eiusmod tempor incididunt ut labore</p>
</main>
</body>
</html>
```